Business Card Design Project

Business card design using our logo, consistent with website branding (www.brightvane.com.au) and includes our services:

advertising|sales|events|production

Details Required:

Dorian Webb
Managing Director

P 1300 586 231
M 0404 827 659
F (02) 9613 2048
E dorian@brightvane.com.au
W www.brightvane.com.au

Will be printed on high quality card with rounded corners.

Quick turnaround required, on standby for any questions to assist with this.

Will upload logo and previous drafts we didn't think were the right fit.

Target Market(s)

Senior business decision-makers

Industry/Entity Type

Business

Requirements
Must have
• Editable template, so details can be updated for staff

Must be in print ready format - please see specs I have just uploaded

```html
<!DOCTYPE html>
<html lang="en">
<head>
<meta charset="utf-8">
<title>BrightVane Business Card</title>
<link href="https://fonts.googleapis.com/css2?family=Jost:wght@400;500&display=swap" rel="stylesheet">
<style>
  :root {
    --page-bg: #ffffff;
    --card-center: #ffffff;
    --card-edge: #e4e4e4;
    --ink: #1a1a1a;
    --accent: #f07a1e;
    --accent-soft: #f9b27a;
    --blue-soft: #9fd3f2;
    --shadow: rgba(0, 0, 0, 0.22);
  }
  * { box-sizing: border-box; margin: 0; padding: 0; }
  html, body {
    width: 1200px; height: 900px; overflow: hidden;
    background: var(--page-bg);
    font-family: "Jost", "Futura", sans-serif;
    color: var(--ink);
  }
  .canvas { position: relative; width: 1200px; height: 900px; }
  .card {
    position: absolute; left: 328px; width: 525px; height: 300px;
    border-radius: 40px;
    background: radial-gradient(ellipse at 50% 45%, var(--card-center) 45%, var(--card-edge) 100%);
    box-shadow: 0 4px 14px var(--shadow), 0 0 3px rgba(0,0,0,0.08);
  }
  .card--front { top: 100px; }
  .card--back { top: 472px; }

  .brand { position: absolute; display: flex; align-items: center; }
  .brand__dot { border-radius: 50%; background: var(--accent); }
  .brand__name { font-weight: 400; color: var(--ink); }

  .card--front .brand { left: 0; right: 0; top: 118px; justify-content: center; gap: 14px; }
  .card--front .brand__dot { width: 34px; height: 34px; }
  .card--front .brand__name { font-size: 44px; letter-spacing: 0.5px; }

  .services {
    position: absolute; left: 0; right: 0; top: 260px;
    text-align: center; font-size: 15.5px; letter-spacing: 0.2px;
  }

  .card--back .brand { left: 35px; top: 44px; gap: 8px; }
  .card--back .brand__dot { width: 18px; height: 18px; }
  .card--back .brand__name { font-size: 23px; }

  .person { position: absolute; left: 35px; top: 120px; }
  .person__name { font-size: 15.5px; line-height: 1.2; }
  .person__title { font-size: 12.5px; color: var(--accent); margin-top: 3px; }

  .contact { position: absolute; left: 35px; top: 197px; list-style: none; font-size: 12.5px; line-height: 16.8px; }
  .contact__label { color: var(--accent); margin-right: 3px; }

  .accent-circle { position: absolute; left: 280px; top: 60px; width: 190px; height: 190px; }
</style>
</head>
<body>
<main class="canvas">
  <section class="card card--front" aria-label="Card front">
    <div class="brand">
      <span class="brand__dot"></span>
      <span class="brand__name">BrightVane</span>
    </div>
    <p class="services">ADVERTISING | SALES | EVENTS | PRODUCTION</p>
  </section>

  <section class="card card--back" aria-label="Card back">
    <div class="brand">
      <span class="brand__dot"></span>
      <span class="brand__name">BrightVane</span>
    </div>
    <div class="person">
      <p class="person__name">Dorian Webb</p>
      <p class="person__title">Managing Director</p>
    </div>
    <ul class="contact">
      <li><span class="contact__label">P</span>1300 586 231</li>
      <li><span class="contact__label">M</span>0404 827 659</li>
      <li><span class="contact__label">F</span>(02) 9613 2048</li>
      <li><span class="contact__label">E</span>dorian@brightvane.com.au</li>
      <li><span class="contact__label">W</span>www.brightvane.com.au</li>
    </ul>
    <svg class="accent-circle" viewBox="0 0 190 190" aria-hidden="true">
      <defs>
        <linearGradient id="circleFill" x1="0" y1="1" x2="1" y2="0">
          <stop offset="0" stop-color="var(--accent-soft)" stop-opacity="0.55"/>
          <stop offset="1" stop-color="var(--blue-soft)" stop-opacity="0.55"/>
        </linearGradient>
      </defs>
      <circle cx="95" cy="95" r="90" fill="url(#circleFill)"/>
    </svg>
  </section>
</main>
</body>
</html>
```